Roble Dorado superhero master

Full website makeover/update and redesign About a Public Figure.. in Spanish as well as English.
See current website at RobleDorado.example and facebook page GoldenOakers .
you can use any of the pictures and videos and be creative. page will be in English and Spanish same design.
think about a Zen Superhero, like Tav from the lattice, with secret mystic knowledge, a combination of the character "Captain Vesper" mixed with the Millionaire Hawk of harbor lane. Themes related to Mentor, based on zodiac, about Financial abundance using the stock Market.

Target Market(s)

USA hispanics Market

Number of Pages Required

5+ page

Colors

Designer to choose colors to be used in the design.

Requirements
Must have
• think about a Zen Superhero, like Tav from the lattice, with secret mystic knowledge, a combination of the character "Captain Vesper" mixed with the Millionaire Hawk of harbor lane. Themes related to Mentor, based on zodiac, about Financial abundance using the stock Market. Surprise me :)
Nice to have
• think about a Zen Superhero, like Tav from the lattice, with secret mystic knowledge, a combination of the character "Captain Vesper" mixed with the hawk of harbor lane.

```html
<!DOCTYPE html>
<html lang="en">
<head>
<meta charset="utf-8">
<title>GoldenOakers — Plan, Execute, Profit</title>
<link rel="stylesheet" href="https://fonts.googleapis.com/css2?family=Roboto:wght@300;400;500;700&family=Roboto+Slab:wght@700;900&display=swap">
<style>
  :root{
    --space-deep:#05071a;
    --gold:#f5a623;
    --gold-light:#f7c14a;
    --icon-gold:#f5c24a;
    --orange-band:#f6a91d;
    --orange-deep:#e88a10;
    --btn-orange:#f28a1e;
    --white:#ffffff;
    --text-soft:#fff3d6;
    --green-top:#8fd15a;
    --green-bottom:#3f9a1c;
    --red-top:#e3474f;
    --red-bottom:#a70f22;
    --card-btn:#f3b44e;
    --footer:#000000;
    --money-dark:#4b4a3a;
    --video-frame:#ffffff;
  }
  *{box-sizing:border-box;margin:0;padding:0}
  html,body{width:1200px;height:2826px;overflow:hidden;background:var(--footer)}
  body{position:relative;font-family:"Roboto",Arial,sans-serif;color:var(--white)}
  .section{position:absolute;left:0;width:1200px;overflow:hidden}

  /* Hero */
  .hero{top:0;height:669px;background:
    radial-gradient(circle at 200px 470px,rgba(255,140,40,.55),transparent 220px),
    radial-gradient(circle at 840px 360px,rgba(120,70,255,.55),transparent 380px),
    radial-gradient(circle at 1100px 120px,rgba(40,110,255,.35),transparent 260px),
    linear-gradient(135deg,#0a0b22 0%,#1a1248 50%,#0b1035 100%)}
  .brand{position:absolute;left:113px;top:22px;display:flex;align-items:center;gap:14px}
  .brand-mark{width:56px;height:56px;border-radius:50%;background:var(--gold)}
  .brand-name{font-family:"Roboto Slab",Georgia,serif;font-weight:900;font-size:38px;line-height:1;color:var(--gold);letter-spacing:1px}
  .phone{position:absolute;left:922px;top:20px;font-size:19px;display:flex;align-items:center;gap:8px}
  .main-nav{position:absolute;left:528px;top:70px;display:flex;align-items:center;gap:38px;font-size:16px;text-transform:uppercase}
  .main-nav .signup{border:2px solid var(--white);padding:8px 18px}
  .hero-title{position:absolute;left:128px;top:246px;font-weight:400;font-size:50px;line-height:52px;color:var(--gold);text-transform:uppercase}
  .hero-sub{position:absolute;left:128px;top:360px;font-size:30px;text-transform:uppercase;font-weight:400}
  .btn{display:inline-block;background:var(--btn-orange);color:var(--white);text-align:center}
  .hero-btn{position:absolute;left:128px;top:421px;width:188px;height:46px;line-height:46px;font-size:18px}
  .hero-portrait{position:absolute;left:606px;top:126px;width:460px;height:460px;border-radius:50%;border:7px solid var(--white);background:linear-gradient(160deg,#cfd3da,#6d6a72 55%,#2a2636)}
  .dots{position:absolute;left:565px;top:627px;display:flex;gap:10px}
  .dots span{width:14px;height:14px;border-radius:50%;background:#d9d9d9}
  .dots span:first-child{background:transparent;border:2px solid #d9d9d9}

  /* How it works */
  .how{top:669px;height:508px;background:
    radial-gradient(circle at 600px 90px,rgba(60,200,255,.35),transparent 300px),
    radial-gradient(circle at 1050px 260px,rgba(110,60,220,.55),transparent 300px),
    linear-gradient(180deg,#17154d 0%,#2a1f6e 60%,#3a2680 100%)}
  .section-title{position:absolute;left:0;width:1200px;text-align:center;font-size:28px;font-weight:400;text-transform:uppercase}
  .how .section-title{top:52px}
  .step{position:absolute;top:120px;width:310px;height:310px;border-radius:50%;border:4px solid var(--white);background:radial-gradient(circle,#0d1030 0%,#1b1850 70%,#2a2468 100%);text-align:center}
  .step svg{margin-top:58px}
  .step h3{font-size:22px;font-weight:500;margin-top:18px}
  .step p{font-size:20px;line-height:27px;margin-top:6px}
  .step-1{left:119px}.step-2{left:452px}.step-3{left:778px}
  .step-arrow{position:absolute;left:372px;top:224px;z-index:2}

  /* Alerts band */
  .alerts-band{top:1177px;height:496px;background:linear-gradient(90deg,var(--orange-deep),var(--orange-band) 40%,var(--gold-light))}
  .mentor-photo{position:absolute;left:188px;top:0;width:310px;height:496px;background:linear-gradient(180deg,#f0d9b8,#d7b27a 60%,#2a2a2a)}
  .alerts-copy{position:absolute;left:550px;top:70px;width:520px}
  .alerts-copy h2{font-size:35px;font-weight:400;line-height:39px;text-transform:uppercase}
  .alerts-copy h2 small{display:block;font-size:28px}
  .alerts-copy p{font-size:15.5px;line-height:25px;color:var(--text-soft);margin-top:16px}
  .alerts-copy ul{list-style:none;margin-top:18px}
  .alerts-copy li{position:relative;padding-left:22px;font-size:15.5px;line-height:25px;color:var(--text-soft);margin-bottom:12px}
  .alerts-copy li::before{content:"";position:absolute;left:2px;top:8px;border-left:7px solid var(--white);border-top:5px solid transparent;border-bottom:5px solid transparent}

  /* Video */
  .video-band{top:1673px;height:490px;background:radial-gradient(circle at 600px 245px,#1a1a14 0%,var(--money-dark) 45%,#7b7a62 100%)}
  .video-frame{position:absolute;left:285px;top:69px;width:646px;height:366px;border:6px solid var(--video-frame);background:linear-gradient(180deg,#7d8a96,#b5b9a8 50%,#5a5f55)}
  .play{position:absolute;left:268px;top:118px;width:100px;height:100px;border-radius:50%;background:#000;border:5px solid var(--white)}
  .video-copy{position:absolute;left:0;top:232px;width:634px;text-align:center;font-family:"Roboto Slab",Georgia,serif;font-weight:700;text-shadow:0 2px 3px #000}
  .video-copy .v1{font-size:21px}
  .video-copy .v2{font-size:17px}
  .video-copy .v3{font-size:12px;font-family:"Roboto",Arial,sans-serif;font-weight:500}
  .video-btn{display:inline-block;margin-top:8px;width:250px;height:48px;line-height:48px;background:linear-gradient(90deg,#b88cf0,#f0d27a);font-size:18px;text-shadow:none}

  /* Services */
  .services{top:2163px;height:462px;background:
    radial-gradient(circle at 160px 240px,rgba(40,140,220,.5),transparent 280px),
    radial-gradient(circle at 1080px 260px,rgba(210,50,110,.55),transparent 300px),
    linear-gradient(90deg,#0d1a4a,#1d1d5c 50%,#4a1d5a)}
  .card{position:absolute;top:109px;width:478px;height:268px;text-align:center;padding:36px 40px 0}
  .card-alerts{left:121px;background:linear-gradient(180deg,var(--green-top),var(--green-bottom))}
  .card-coach{left:607px;background:linear-gradient(180deg,var(--red-top),var(--red-bottom))}
  .card h3{font-size:32px;font-weight:400}
  .card p{font-size:15px;line-height:24.5px;margin-top:8px}
  .card .btn{position:absolute;left:162px;bottom:-12px;width:155px;height:40px;line-height:40px;font-size:14px;background:var(--card-btn);text-transform:uppercase}

  /* Footer */
  .site-footer{top:2625px;height:201px;background:var(--footer);text-align:center}
  .footer-nav{display:flex;justify-content:center;gap:38px;margin-top:50px;font-size:17px;text-transform:uppercase}
  .copyright{font-size:14px;color:#bfbfbf;margin-top:10px}
  .social{display:flex;justify-content:center;gap:10px;margin-top:18px}
  .social span{width:34px;height:34px;border-radius:50%;border:2px solid var(--white)}
</style>
</head>
<body>

<header class="section hero" role="img" aria-label="Starry cosmic background with glowing zodiac wheel and network lines">
  <div class="brand"><span class="brand-mark"></span><span class="brand-name">GOLDENOAKERS</span></div>
  <div class="phone">
    <svg width="18" height="18" viewBox="0 0 24 24"><path d="M6.6 10.8a15.2 15.2 0 0 0 6.6 6.6l2.2-2.2c.3-.3.7-.4 1-.2 1.1.4 2.3.6 3.6.6.6 0 1 .4 1 1V20c0 .6-.4 1-1 1A17 17 0 0 1 3 4c0-.6.4-1 1-1h3.5c.6 0 1 .4 1 1 0 1.3.2 2.5.6 3.6.1.3 0 .7-.2 1z" fill="#fff"/></svg>
    (555) 014-2290
  </div>
  <nav class="main-nav">
    <span>How it works</span><span>About Oak</span><span>Videos</span><span>FAQ</span><span class="signup">Sign up</span>
  </nav>
  <h1 class="hero-title">I turned the<br>stock market</h1>
  <p class="hero-sub">Into my source of income!</p>
  <span class="btn hero-btn">Get Started</span>
  <div class="hero-portrait" role="img" aria-label="Photo of the mentor seated in a modern living room"></div>
  <div class="dots"><span></span><span></span><span></span><span></span></div>
</header>

<section class="section how">
  <h2 class="section-title">How it works</h2>
  <div class="step step-1">
    <svg width="56" height="48" viewBox="0 0 56 48"><path d="M4 4 V44 H52" fill="none" stroke="#f5c24a" stroke-width="5"/><path d="M12 34 L24 20 L32 28 L46 12" fill="none" stroke="#f5c24a" stroke-width="5"/><path d="M38 10 H48 V20" fill="none" stroke="#f5c24a" stroke-width="5"/></svg>
    <h3>STEP 1</h3><p>Learn Right Way<br>to Trade Stock</p>
  </div>
  <div class="step step-2">
    <svg width="60" height="50" viewBox="0 0 60 50"><rect x="2" y="2" width="56" height="36" rx="3" fill="#f5c24a"/><rect x="8" y="8" width="44" height="24" fill="#151340"/><rect x="24" y="38" width="12" height="6" fill="#f5c24a"/><rect x="16" y="44" width="28" height="4" fill="#f5c24a"/></svg>
    <h3>STEP 2</h3><p>Practice on a Demo<br>Account &amp; See My Alerts</p>
  </div>
  <div class="step step-3">
    <svg width="62" height="50" viewBox="0 0 62 50"><circle cx="31" cy="12" r="9" fill="#f5c24a"/><circle cx="12" cy="18" r="7" fill="#f5c24a"/><circle cx="50" cy="18" r="7" fill="#f5c24a"/><path d="M16 48 Q16 26 31 26 Q46 26 46 48Z" fill="#f5c24a"/><path d="M0 48 Q0 30 12 30 Q18 30 20 34 Q14 40 14 48Z" fill="#f5c24a"/><path d="M62 48 Q62 30 50 30 Q44 30 42 34 Q48 40 48 48Z" fill="#f5c24a"/></svg>
    <h3>STEP 3</h3><p>Earn Thousands and<br>Enjoy the Life you deserve</p>
  </div>
  <svg class="step-arrow" width="130" height="46" viewBox="0 0 130 46"><path d="M4 40 Q60 -6 118 30" fill="none" stroke="#fff" stroke-width="3" stroke-dasharray="3 6"/><path d="M106 32 L120 32 L115 18" fill="none" stroke="#fff" stroke-width="3"/></svg>
</section>

<section class="section alerts-band">
  <div class="mentor-photo" role="img" aria-label="Photo of the mentor standing with arms crossed, white shirt and suspenders"></div>
  <div class="alerts-copy">
    <h2>8 out of 10 of my alerts<small>go up 20% same day</small></h2>
    <p>Did you know that today over 50 different companies on the stock market went up 20-300%? This happens every day and I can show you how to turn the Stock Market into your own private business. My goal is to help you make more money.<br>Here is how you can benefit:</p>
    <ul>
      <li>I do the research and invest my own money, sending a text alert telling you what I just bought/sold.</li>
      <li>This info, you may include in your own research or you may duplicate my trades.</li>
    </ul>
  </div>
</section>

<section class="section video-band" role="img" aria-label="Tunnel of swirling banknotes">
  <div class="video-frame" role="img" aria-label="Video still of the mentor with arms open in stadium seating">
    <span class="play"><svg width="90" height="90" viewBox="0 0 90 90"><path d="M36 26 L62 45 L36 64Z" fill="#fff"/></svg></span>
    <div class="video-copy">
      <div class="v1">A NEW INVESTMENT EXPERIENCE!</div>
      <div class="v2">CONVENIENCE, MORE CONTROL &amp; BETTER PROFITS!</div>
      <div class="v3">With the OakAlerts &amp; OakCoach system, you can make thousands in minutes!</div>
      <span class="video-btn">START TODAY!</span>
    </div>
  </div>
</section>

<section class="section services">
  <article class="card card-alerts">
    <h3>OakAlerts!</h3>
    <p>With OakAlerts*** you know exactly when I get in and out of my trades. Take advantage of the Free Training class for subscribers, a great tool for new traders or those with some experience. You can expect 1-3 Alerts per day on Stocks under $10</p>
    <span class="btn">Read more</span>
  </article>
  <article class="card card-coach">
    <h3>OakCoach!</h3>
    <p>Is not about the Money. Is about your super power!<br>That's the secret you learn One on One with The GoldenOaker. With a personalized analysis covering the Law of Attraction in your life, GoldenOaker pinpoints</p>
    <span class="btn">Read more</span>
  </article>
</section>

<footer class="section site-footer">
  <nav class="footer-nav"><span>Home</span><span>How it works</span><span>About Oak</span><span>Videos</span><span>FAQ</span><span>Sign up</span></nav>
  <p class="copyright">© 2017 Company Name&nbsp; All right reserved</p>
  <div class="social"><span></span><span></span><span></span><span></span></div>
</footer>

</body>
</html>
```